Ashby Meadows Summer Swim Bag Tag Design

Hello!

We are looking to design a 2-sided bag tag for a children's summer swim team. Colors should be blue, white, pink. May also use a lighter blue or navy as an accent if needed. Attached are 2 files showing the look/feel of some of our other items. The bag tag would need to be in line with this same look.

Copy: Ashby Meadows Otters Swim 2026
#paddleon

The copy can be both on one side, or split between the 2 sides, either works. We are flexible! Needs to incorporate the 2026 logo into the design.

```html
<!DOCTYPE html>
<html lang="en">
<head>
<meta charset="utf-8">
<title>Ashby Meadows Otters Swim 2026 – Bag Tag</title>
<link rel="stylesheet" href="https://fonts.googleapis.com/css2?family=Fredoka:wght@600;700&family=Lilita+One&display=swap">
<style>
  :root {
    --royal: #1f55b4;
    --navy: #163f8c;
    --sky: #86c0f0;
    --pink: #f06aa6;
    --white: #ffffff;
    --page: #ffffff;
  }
  * { margin: 0; padding: 0; box-sizing: border-box; }
  html, body {
    width: 1200px;
    height: 720px;
    overflow: hidden;
    background: var(--page);
  }
  .canvas {
    position: relative;
    width: 1200px;
    height: 720px;
  }
  .bag-tag {
    position: absolute;
    top: 118px;
    width: 540px;
    height: 582px;
  }
  .bag-tag--front { left: 46px; }
  .bag-tag--back { left: 620px; }
  .bag-tag svg { display: block; width: 100%; height: 100%; }

  .tag-body { fill: var(--royal); }
  .tag-slot { fill: var(--white); }

  .team-name {
    font-family: "Lilita One", sans-serif;
    font-size: 46px;
    fill: var(--white);
    stroke: var(--navy);
    stroke-width: 9px;
    paint-order: stroke;
    stroke-linejoin: round;
  }
  .mascot-name {
    font-family: "Lilita One", sans-serif;
    font-size: 118px;
    fill: var(--sky);
    stroke: var(--navy);
    stroke-width: 11px;
    paint-order: stroke;
    stroke-linejoin: round;
  }
  .swim-word {
    font-family: "Lilita One", sans-serif;
    font-size: 84px;
    fill: var(--pink);
    stroke: var(--white);
    stroke-width: 9px;
    paint-order: stroke;
    stroke-linejoin: round;
  }
  .season-year {
    font-family: "Fredoka", sans-serif;
    font-weight: 700;
    font-size: 98px;
    fill: var(--sky);
    stroke: var(--white);
    stroke-width: 9px;
    paint-order: stroke;
    stroke-linejoin: round;
  }
  .hashtag {
    font-family: "Fredoka", sans-serif;
    font-weight: 700;
    font-size: 36px;
    fill: var(--white);
  }
  .hashtag-rule {
    stroke: var(--pink);
    stroke-width: 5px;
    stroke-linecap: round;
  }
  .year-badge { fill: var(--pink); }
  .year-digit {
    font-family: "Fredoka", sans-serif;
    font-weight: 700;
    font-size: 250px;
    stroke-width: 7px;
    paint-order: stroke;
    stroke-linejoin: round;
  }
  .year-digit--white { fill: var(--white); stroke: var(--pink); }
  .year-digit--pink { fill: var(--pink); stroke: var(--white); }
  .year-digit--sky { fill: var(--sky); stroke: var(--white); }
  .club-seal { fill: var(--white); }
  .club-name {
    font-family: "Fredoka", sans-serif;
    font-weight: 600;
    font-size: 20px;
    fill: var(--royal);
  }
</style>
</head>
<body>
<main class="canvas">

  <section class="bag-tag bag-tag--front" aria-label="Bag tag front">
    <svg viewBox="0 0 540 582" xmlns="http://www.w3.org/2000/svg">
      <defs>
        <radialGradient id="front-wash" cx="50%" cy="46%" r="68%">
          <stop offset="0%" stop-color="#f27bb2"/>
          <stop offset="55%" stop-color="#d86aa9"/>
          <stop offset="85%" stop-color="#7d62b8"/>
          <stop offset="100%" stop-color="#2f5bbd"/>
        </radialGradient>
        <linearGradient id="mascot-fill" x1="0" y1="0" x2="0" y2="1">
          <stop offset="0%" stop-color="#2a63c4"/>
          <stop offset="70%" stop-color="#5d8fd8"/>
          <stop offset="100%" stop-color="#eef5fd"/>
        </linearGradient>
      </defs>
      <rect class="tag-body" x="0" y="0" width="540" height="582" rx="26"/>
      <rect x="10" y="10" width="520" height="480" rx="18" fill="url(#front-wash)"
            role="img" aria-label="Pink and blue rippling water-line pattern"/>
      <rect class="tag-slot" x="214" y="20" width="112" height="30" rx="15"/>

      <text class="team-name" x="272" y="130" text-anchor="middle" transform="rotate(-4 272 112)">ASHBY MEADOWS</text>
      <text class="mascot-name" x="278" y="244" text-anchor="middle" transform="rotate(-4 278 200)">OTTERS</text>

      <rect x="62" y="262" width="196" height="206" rx="70" fill="url(#mascot-fill)"
            role="img" aria-label="Leaping otter mascot illustration above a water splash"/>

      <text class="swim-word" x="360" y="314" text-anchor="middle" transform="rotate(-4 360 290)">SWIM</text>
      <text class="season-year" x="362" y="410" text-anchor="middle" transform="rotate(-4 362 375)">2026</text>

      <line class="hashtag-rule" x1="46" y1="519" x2="166" y2="519"/>
      <line class="hashtag-rule" x1="374" y1="519" x2="494" y2="519"/>
      <text class="hashtag" x="270" y="532" text-anchor="middle">#paddleon</text>
    </svg>
  </section>

  <section class="bag-tag bag-tag--back" aria-label="Bag tag back">
    <svg viewBox="0 0 540 582" xmlns="http://www.w3.org/2000/svg">
      <defs>
        <radialGradient id="back-wash" cx="50%" cy="46%" r="68%">
          <stop offset="0%" stop-color="#7db4ea"/>
          <stop offset="60%" stop-color="#4f86d6"/>
          <stop offset="100%" stop-color="#2658b6"/>
        </radialGradient>
      </defs>
      <rect class="tag-body" x="0" y="0" width="540" height="582" rx="26"/>
      <rect x="10" y="10" width="520" height="480" rx="18" fill="url(#back-wash)"
            role="img" aria-label="Light blue rippling water-line pattern"/>
      <rect class="tag-slot" x="214" y="20" width="112" height="30" rx="15"/>

      <g class="year-badge">
        <rect x="50" y="96" width="382" height="400" rx="50"/>
        <circle cx="346" cy="170" r="116"/>
      </g>

      <text class="year-digit year-digit--white" x="168" y="275" text-anchor="middle">2</text>

      <circle class="club-seal" cx="346" cy="170" r="100"/>
      <text class="club-name" x="346" y="162" text-anchor="middle">ASHBY MEADOWS</text>
      <text class="club-name" x="346" y="190" text-anchor="middle">SWIM &amp; DIVE</text>

      <text class="year-digit year-digit--pink" x="192" y="456" text-anchor="middle">2</text>
      <text class="year-digit year-digit--sky" x="346" y="456" text-anchor="middle">6</text>

      <line class="hashtag-rule" x1="46" y1="519" x2="166" y2="519"/>
      <line class="hashtag-rule" x1="374" y1="519" x2="494" y2="519"/>
      <text class="hashtag" x="270" y="532" text-anchor="middle">#paddleon</text>
    </svg>
  </section>

</main>
</body>
</html>
```